DL Flyer for vehicle buying/selling service and advice business

New business to help people sell their current vehicle then select and buy and maintain their next car. (New or used).
We'll prepare and sell your car for you and get $,000s more than a trade in.
Offer advice as to the best car currently on the market based on our customer's needs.
With country wide sourcing network of cars across all manufacturers we have great buying power to ensure the very best possible price.
Personal service, including preparation of car for sale, pickup of old and drop-off of new vehicles, organise RWC and any required repairs.
We are NOT a car dealer so we WILL not try to sell you the vehicles we own.
Totally impartial, professional and friendly service making the purchase of your next car a great experience.
Updates

Flyer wording===========“Don’t sell your car or buy your next car without speaking to us”We guarantee to get you a better price for your current car and to find a cheaper purchase price for your next car.With a country wide sourcing network of cars “new and used” across all manufacturers we have sensational buying power to ensure the very best possible price.We can source the right car on any budget, from $2,000 to $200,000We are NOT a car dealer so we WILL not try to sell you the vehicles we own.By not being affiliated with any individual car manufacturer or dealer we can offer absolute impartiality.We’ll sit with you to discuss the best car for your needs and even bring the car to you for a test drive without the pressure of a salesperson nearby.Our services include:• Selling your current car: - Obtaining a roadworthy certificate - Organising any repairs needed - Detailing your car (wash, vacuum, polish) - Advertising of your car - Dealing with potential buyers - Negotiating the best price on your behalf• Assisting with the selection of your next car• Organising test drives• Purchasing the car of your choice - Sourcing the very best price• Ongoing management of their vehicle (service, clean, repair)Possible inclusions in the flyer might be:Advantages of upgrading to a new vehicle include:o reliability, o safety,o fuel efficiencyo comfort.Space for a couple of short testimonials Background images of all of the major car manufacturers Added Friday, July 29, 2016

Target Market(s)

Local community.
Initially will drop DL flyers in local post boxes

Industry/Entity Type

Business

Requirements
Must have
• Flyer wording:
• ===========
• “Don’t sell your car or buy your next car without speaking to us”
• ---------------------------------------------------------------------------------
• We guarantee to get you a better price for your current car and to find a cheaper purchase price for your next car.
• With a country wide sourcing network of cars “new and used” across all manufacturers we have sensational buying power to ensure the very best possible price.
• We can source the right car on any budget, from $2,000 to $200,000
• We are NOT a car dealer so we WILL not try to sell you the vehicles we own.
• By not being affiliated with any individual car manufacturer or dealer we can offer absolute impartiality.
• We’ll sit with you to discuss the best car for your needs and even bring the car to you for a test drive without the pressure of a salesperson nearby.
• Our services include:
• • Selling your current car:
• o Obtaining a roadworthy certificate
• o Organising any repairs needed
• o Detailing your car (wash, vacuum, polish)
• o Advertising of your car
• o Dealing with potential buyers
• o Negotiating the best price on your behalf
• • Assisting with the selection of your next car
• • Organising test drives
• • Purchasing the car of your choice
• o Sourcing the very best price
• • Ongoing management of your vehicle (service, clean, repair)
• Call Gerald on: 0427 315064
Nice to have
• Possible inclusions on the flyer might be:
• List of advantages of upgrading to a new vehicle:
• o reliability,
• o safety,
• o fuel efficiency
• o comfort
• Space for a couple of short testimonials
• Background images of all of the major car manufacturers

```html
<!DOCTYPE html>
<html lang="en">
<head>
<meta charset="utf-8">
<title>Autowise Direct – DL Flyer</title>
<link rel="stylesheet" href="https://fonts.googleapis.com/css2?family=Archivo:wght@800&family=Exo+2:wght@400;600;700&display=swap">
<style>
  :root {
    --backdrop: #e6e6e6;
    --orange: #e07a1f;
    --orange-deep: #c9620f;
    --brown-red: #8a2a0c;
    --ink: #1c1c1c;
    --paper: #ffffff;
    --grey-photo-a: #f2f2f2;
    --grey-photo-b: #cfcfcf;
  }
  * { box-sizing: border-box; margin: 0; padding: 0; }
  html, body { width: 1200px; height: 1198px; overflow: hidden; }
  body { background: var(--backdrop); font-family: "Exo 2", sans-serif; position: relative; }

  .panel {
    position: absolute; top: 69px; width: 500px; height: 1060px;
    background: var(--paper); overflow: hidden;
    box-shadow: 0 4px 14px rgba(0,0,0,.18);
  }
  .panel--front { left: 60px; }
  .panel--back { left: 640px; background: var(--orange); }

  /* ---------- front ---------- */
  .front-photo-top {
    position: absolute; left: 0; top: 0; width: 100%; height: 600px;
    background: linear-gradient(160deg, var(--grey-photo-a) 0%, #e2e2e2 55%, var(--grey-photo-b) 100%);
  }
  .brand { position: absolute; left: 40px; top: 76px; }
  .brand__name { font-family: "Exo 2", sans-serif; font-weight: 600; font-size: 36px; color: var(--ink); }

  .headline {
    position: absolute; left: 40px; top: 170px;
    font-family: "Archivo", sans-serif; font-weight: 800; font-size: 42px; line-height: 1.12;
    color: var(--ink); text-transform: uppercase;
  }
  .tagline {
    position: absolute; left: 40px; top: 420px;
    font-family: "Archivo", sans-serif; font-weight: 800; font-size: 38px; line-height: 1.12;
    color: var(--orange); text-transform: uppercase;
  }
  .front-curve { position: absolute; left: 0; top: 520px; width: 100%; height: 120px; }
  .front-photo-main {
    position: absolute; left: 0; top: 610px; width: 100%; height: 380px;
    background: linear-gradient(135deg, #5a4a3e 0%, #b89a74 45%, #e8dccb 100%);
  }
  .call-band {
    position: absolute; left: 0; bottom: 0; width: 100%; height: 80px;
    background: var(--orange); display: flex; align-items: center; justify-content: center;
    font-family: "Archivo", sans-serif; font-weight: 800; font-size: 40px; color: var(--paper);
  }

  /* ---------- back ---------- */
  .back-photo-top {
    position: absolute; left: 0; top: 0; width: 100%; height: 420px;
    background: linear-gradient(120deg, #d9dce6 0%, #a7b3cf 40%, #c59a7a 70%, #f1ece4 100%);
  }
  .back-curve { position: absolute; left: 0; top: 330px; width: 100%; height: 130px; }
  .hex-photo { position: absolute; right: 40px; top: 300px; width: 200px; height: 190px; }

  .services-title {
    position: absolute; left: 30px; top: 430px;
    font-weight: 700; font-size: 34px; color: var(--brown-red);
  }
  .service-list { position: absolute; list-style: none; color: var(--paper); font-size: 18px; line-height: 1.3; }
  .service-list li { position: relative; padding-left: 16px; margin-bottom: 12px; }
  .service-list li::before {
    content: ""; position: absolute; left: 0; top: 9px; width: 6px; height: 6px;
    border-radius: 50%; background: var(--brown-red);
  }
  .service-list--sell { left: 30px; top: 490px; width: 235px; }
  .service-list--buy { left: 270px; top: 550px; width: 228px; }

  .cars-tab {
    position: absolute; left: 200px; top: 905px; padding: 2px 14px;
    background: var(--brown-red); color: var(--paper); font-weight: 700; font-size: 24px;
  }
  .cars-grid {
    position: absolute; left: 20px; top: 935px; width: 460px; height: 110px;
    background: var(--paper); padding: 4px;
    display: grid; grid-template-columns: repeat(9, 1fr); grid-template-rows: repeat(3, 1fr); gap: 0;
  }
  .cars-grid span { display: block; }
  .cars-grid .dark { background: #111; }
  .cars-grid .light { background: var(--paper); }
  .cars-grid span::after { content: ""; display: block; width: 40%; height: 40%; margin: 30% auto 0; border-radius: 50%; background: #9a9a9a; }
</style>
</head>
<body>

<section class="panel panel--front">
  <div class="front-photo-top" role="img" aria-label="Faded black and white photo of a family loading an open car boot"></div>
  <div class="brand">
    <span class="brand__name">Autowise Direct</span>
  </div>
  <h1 class="headline">Before you sell<br>your car or<br>buy a new car<br>call us</h1>
  <p class="tagline">We will get you<br>a better price</p>
  <svg class="front-curve" viewBox="0 0 500 120" preserveAspectRatio="none" aria-hidden="true">
    <path d="M0 75 Q250 110 500 20 L500 120 L0 120 Z" fill="var(--orange)"/>
    <path d="M0 95 Q250 125 500 45 L500 120 L0 120 Z" fill="var(--paper)"/>
  </svg>
  <div class="front-photo-main" role="img" aria-label="Photo of a delighted woman leaning out of a car window holding up its keys"></div>
  <div class="call-band">Call 0427 315064</div>
</section>

<section class="panel panel--back">
  <div class="back-photo-top" role="img" aria-label="Photo of a smiling couple reviewing paperwork with a consultant"></div>
  <svg class="back-curve" viewBox="0 0 500 130" preserveAspectRatio="none" aria-hidden="true">
    <path d="M0 70 Q250 10 500 60 L500 130 L0 130 Z" fill="var(--paper)"/>
    <path d="M0 85 Q250 25 500 75 L500 130 L0 130 Z" fill="var(--orange)"/>
  </svg>
  <svg class="hex-photo" viewBox="0 0 200 190" role="img" aria-label="Hexagon photo of two happy women in their new car">
    <polygon points="50,4 150,4 198,95 150,186 50,186 2,95" fill="var(--paper)"/>
    <polygon points="54,12 146,12 189,95 146,178 54,178 11,95" fill="#8b7a70"/>
  </svg>

  <h2 class="services-title">Our services</h2>
  <ul class="service-list service-list--sell">
    <li>Selling your current car</li>
    <li>Obtaining a roadworthy certificate</li>
    <li>Organising any repairs needed</li>
    <li>Detailing your car (wash, vacuum, polish)</li>
    <li>Advertising of your car</li>
    <li>Dealing with potential buyers</li>
    <li>Negotiating the best price on your behalf</li>
  </ul>
  <ul class="service-list service-list--buy">
    <li>Assisting with the selection of your next car</li>
    <li>Organising test drives</li>
    <li>Purchasing the car of your choice</li>
    <li>Sourcing the very best price</li>
    <li>Ongoing management of your vehicle (service, clean, repair)</li>
  </ul>

  <div class="cars-grid" aria-label="Car makes on offer">
    <span class="light"></span><span class="dark"></span><span class="light"></span><span class="dark"></span><span class="light"></span><span class="dark"></span><span class="light"></span><span class="dark"></span><span class="light"></span>
    <span class="dark"></span><span class="light"></span><span class="dark"></span><span class="light"></span><span class="dark"></span><span class="light"></span><span class="dark"></span><span class="light"></span><span class="dark"></span>
    <span class="light"></span><span class="dark"></span><span class="light"></span><span class="dark"></span><span class="light"></span><span class="dark"></span><span class="light"></span><span class="dark"></span><span class="light"></span>
  </div>
  <div class="cars-tab">Cars we offer</div>
</section>

</body>
</html>
```